Classic and neutral book cover design

We are looking for a classic and neutral book cover design to be used as the template for a series of books to be published. We are hence looking for a template that will allow us to easily change the title name for all books in this series.
The use of very few colours (black and white is welcome) and few design elements is a big bonus. As a source of inspiration we would like to ask you to view the very simple and
If you think you have a cool idea that can add a twist to the formal classic look don't hesitate. Go for it !
Work will be done for a 30 year old Sweden based cultural non-profit called VĂ©ru (www.veruhaus-example.org). We work with the publishing and supporting of post-modern art and literature addressing contemporary topics but are also involved in assisting projects of cultural preservation.
Target Market(s)
The audience is expected to have some form of interest in culture but could range from hobbyist readers to tenure track scholars
Industry/Entity Type
Non-Profit
Requirements
Must have
- General:
- Classic and neutral feel
- Preferably very simple and few shapes
- usage of few colours (black and white is welcome)
Information to be displayed on the cover is:
- Author
- Title
- type of work e.g. play/novel (optional)
- publishing house (in this case "Veru Publishing")
Nice to have
- ideas to prevent it from become boring are of course welcome
Should not have
- - too many colours

```html
<!DOCTYPE html>
<html lang="en">
<head>
<meta charset="utf-8">
<title>Véru Publishing – Series Covers</title>
<link rel="stylesheet" href="https://fonts.googleapis.com/css2?family=Archivo:wght@700;800&family=Archivo+Narrow:wght@400;700&display=swap">
<style>
  :root {
    --page: #ffffff;
    --blue: #93c2d8;
    --magenta: #ec008c;
    --yellow: #fff200;
    --ink: #231f20;
    --white: #ffffff;
    --shadow: rgba(0, 0, 0, 0.28);
  }
  html, body {
    margin: 0;
    padding: 0;
    width: 1200px;
    height: 900px;
    overflow: hidden;
    background: var(--page);
  }
  .series {
    position: relative;
    width: 1200px;
    height: 900px;
  }
  .cover {
    position: absolute;
    top: 204px;
    width: 335px;
    height: 423px;
    overflow: hidden;
    box-shadow: 4px 4px 6px var(--shadow);
    color: var(--ink);
    font-family: "Archivo Narrow", "Arial Narrow", sans-serif;
  }
  .cover--nonfiction { left: 57px; background: var(--blue); }
  .cover--fiction { left: 426px; background: var(--magenta); color: var(--white); }
  .cover--poetry { left: 791px; background: var(--yellow); }

  .cover__author {
    position: absolute;
    top: 58px;
    left: 0;
    right: 0;
    text-align: center;
    font-size: 16px;
    font-weight: 400;
  }
  .cover__title {
    position: absolute;
    left: 0;
    right: 0;
    margin: 0;
    text-align: center;
    font-family: "Archivo", "Arial", sans-serif;
    font-weight: 700;
    text-transform: uppercase;
  }
  .cover__title--long {
    top: 173px;
    font-size: 22px;
    line-height: 25px;
    letter-spacing: 0.36em;
    padding-left: 0.36em;
  }
  .cover__title--short {
    top: 188px;
    font-size: 35px;
    line-height: 44px;
    letter-spacing: 0.42em;
    padding-left: 0.42em;
  }
  .cover__subtitle {
    position: absolute;
    top: 228px;
    left: 0;
    right: 0;
    text-align: center;
    font-size: 16px;
  }
  .cover__genre-mark {
    position: absolute;
    top: 250px;
    font-family: "Archivo", "Arial", sans-serif;
    font-weight: 800;
    font-size: 212px;
    line-height: 1;
    color: var(--white);
  }
  .cover--nonfiction .cover__genre-mark { left: 205px; }
  .cover--fiction .cover__genre-mark { left: 229px; }
  .cover--poetry .cover__genre-mark { left: 212px; }

  .cover__publisher {
    position: absolute;
    top: 386px;
    left: 140px;
    font-family: "Archivo Narrow", "Arial Narrow", sans-serif;
    font-size: 17px;
    font-weight: 400;
    color: var(--ink);
    letter-spacing: 0.02em;
  }
</style>
</head>
<body>
  <main class="series">
    <article class="cover cover--nonfiction">
      <div class="cover__author">Aurèle Fontvieille</div>
      <h1 class="cover__title cover__title--long">Lighthouse<br>and Harbour</h1>
      <div class="cover__subtitle">In Coastal Trade 1810-1816</div>
      <div class="cover__genre-mark">N</div>
      <div class="cover__publisher">Véru</div>
    </article>

    <article class="cover cover--fiction">
      <div class="cover__author">Aurèle Fontvieille</div>
      <h1 class="cover__title cover__title--short">Title</h1>
      <div class="cover__genre-mark">F</div>
      <div class="cover__publisher">Véru</div>
    </article>

    <article class="cover cover--poetry">
      <div class="cover__author">Aurèle Fontvieille</div>
      <h1 class="cover__title cover__title--short">Title</h1>
      <div class="cover__genre-mark">P</div>
      <div class="cover__publisher">Véru</div>
    </article>
  </main>
</body>
</html>
```